Sponsorship Letter and Brochure showing different levels of sponsorship

I am looking for a Modern /Western themed sponsor letter I have attached the logo and photos we would like to have in the brochure, this will be sent to potential sponsors. I would also like this to be editable. We are an Open Rodeo in the Treaty 8 Nation. I am looking for this to be neat and tidy with some sort of chart showing what they get for the price they are willing to donate. Keep colours within the logo colours. I have attached numerous photos you can use which ever you like..

Colors
0054AA
0677BA
7BADD7
CADEEF
E8F1F8
00AB8E
00BBA5
67D7C9
C6EFE9
E9F9F6
FFC000
F8CF3A
FAE287
FDF2CF
FEFAEE
EE7325
F08F49
F5BC92
FAE3D3
FDF4ED
EB3D1F
EC4F4E
F09395
F8D3D4
FCEDEE

```html
<!DOCTYPE html>
<html lang="en">
<head>
<meta charset="utf-8">
<title>Cedar Ridge Rodeo – Sponsorship Package</title>
<link href="https://fonts.googleapis.com/css2?family=Rye&family=Oswald:wght@600&family=Arimo:ital,wght@0,400;0,700;1,400&display=swap" rel="stylesheet">
<style>
  :root{
    --board:#a7a6ab;
    --paper:#ffffff;
    --ink:#1c1c1c;
    --brown:#3b2412;
    --orange:#d88c45;
    --charcoal:#2b2a2c;
    --tan:#efcba2;
    --cream:#f6e8dc;
    --red:#e5432a;
    --blue:#1f72b8;
  }
  *{box-sizing:border-box;margin:0;padding:0}
  html,body{width:925px;height:1200px;overflow:hidden}
  body{background:var(--board);position:relative;font-family:"Arimo",Arial,sans-serif;color:var(--ink)}
  .page{position:absolute;background:var(--paper);overflow:hidden}
  .page-letter{left:278px;top:63px;width:369px;height:522px}
  .page-levels{left:83px;top:609px;width:368px;height:521px}
  .page-events{left:477px;top:609px;width:367px;height:521px}
  .abs{position:absolute}

  .brand{position:absolute;display:flex;flex-direction:column;align-items:center;justify-content:center;text-align:center;gap:3px}
  .brand-dot{width:9px;height:9px;border-radius:50%;background:var(--orange)}
  .brand-name{font-family:"Arimo",Arial,sans-serif;font-weight:700;color:var(--charcoal);line-height:1.05}

  .hero-banner{left:121px;top:28px;width:221px;height:63px;background:var(--orange);border-radius:3px;display:flex;flex-direction:column;align-items:center;justify-content:center;text-align:center;padding-right:26px}
  .hero-banner::before{content:"";position:absolute;inset:3px;border:1px solid rgba(255,255,255,.7);border-radius:2px}
  .hero-line{font-family:"Rye",serif;color:var(--brown);line-height:1.15;white-space:nowrap}
  .hero-line.sm{font-size:9px}
  .hero-line.lg{font-size:11px;color:#fff}
  .rider-art{left:293px;top:0;width:76px;height:124px;background:linear-gradient(160deg,#5a5a5a,#2a2a2a);border-radius:40% 20% 10% 30%;opacity:.85}
  .swirl-art{left:215px;top:435px;width:154px;height:87px;background:radial-gradient(ellipse at 60% 50%,#f6e7da 0%,rgba(246,231,218,0) 70%)}
  .letter{left:22.5px;top:115px;width:327px;font-size:6.5px;line-height:8.2px}
  .letter p{margin-bottom:8.2px}
  .letter .salute{font-weight:700;font-size:7.4px}
  .letter ul{margin:0 0 8.2px 14px;font-weight:700}
  .letter b{font-weight:700}
  .sign{font-weight:700}

  .sheet-title{position:absolute;top:25px;width:124px;text-align:center;font-family:"Rye",serif;color:var(--red);font-size:11.5px;line-height:18px;font-weight:400;white-space:nowrap}
  .bronco-art{position:absolute;top:21px;width:43px;height:41px;background:linear-gradient(135deg,#7bb0db,#1f72b8);border-radius:45% 30% 40% 35%}
  .photo{position:absolute;border:2px dashed #fff;outline:1px solid #222;outline-offset:-1px}
  .tan-block{position:absolute;background:var(--tan)}

  .tier-head{position:absolute;display:flex;align-items:center;justify-content:space-between;padding:0 5px;color:#fff;font-family:"Oswald","Arial Narrow",sans-serif;font-weight:600;font-size:8px;letter-spacing:.4px;white-space:nowrap;border-radius:2px}
  .to-dark{background:linear-gradient(90deg,var(--orange) 0%,var(--orange) 35%,var(--charcoal) 100%)}
  .to-orange{background:linear-gradient(90deg,var(--charcoal) 0%,var(--orange) 75%)}
  .tier-head svg{width:10px;height:10px;flex:none;fill:var(--blue)}
  .tier-body{position:absolute;background:var(--cream);padding:3px 4px 3px 7px;font-size:5.9px;line-height:7.3px}
  .tier-body ul{list-style:none}
  .tier-body li{position:relative;padding-left:6px}
  .tier-body li::before{content:"•";position:absolute;left:0}
  .diamond-body{display:flex;gap:12px;padding-top:5px}
  .diamond-body ul{flex:1}

  .event-head{position:absolute;display:flex;align-items:center;justify-content:space-between;padding:0 8px;color:#fff;font-size:6.2px;line-height:7.4px;text-align:center}
  .event-head span{flex:1}
  .event-head svg{width:11px;height:11px;fill:var(--blue);flex:none}
  .event-body{position:absolute;padding:3px 0 0 3px;font-size:5.9px;line-height:7.3px}
  .event-body ul{list-style:none}
  .event-body li{position:relative;padding-left:7px}
  .event-body li::before{content:"•";position:absolute;left:0}

  .closing{left:22.5px;top:418px;width:323px;font-size:5.8px;line-height:7.3px}
  .quote-box{left:22.5px;top:455px;width:323px;height:42px;background:var(--cream);text-align:center;font-size:6px;line-height:8px;padding-top:3px}
  .quote-box strong{font-size:6.8px;display:block;line-height:8.3px}
  .quote-box em{font-size:5.8px}
  .flourish-art{position:absolute;top:8px;width:45px;height:24px;background:linear-gradient(90deg,rgba(229,67,42,.15),rgba(229,67,42,.45),rgba(229,67,42,.15));border-radius:50%}
</style>
</head>
<body>
<svg width="0" height="0" style="position:absolute" aria-hidden="true">
  <symbol id="star" viewBox="0 0 20 20"><path d="M10 0 12.9 5 18.7 5 15.8 10 18.7 15 12.9 15 10 20 7.1 15 1.3 15 4.2 10 1.3 5 7.1 5Z"/></symbol>
</svg>

<section class="page page-letter">
  <div class="brand" style="left:21px;top:28px;width:77px;height:68px">
    <span class="brand-dot"></span>
    <span class="brand-name" style="font-size:11px">Cedar Ridge<br>Rodeo</span>
  </div>
  <div class="abs hero-banner">
    <div class="hero-line sm">Join Us in Making the</div>
    <div class="hero-line lg">2024 Cedar Ridge Rodeo</div>
    <div class="hero-line sm">Even More Spectacular!</div>
  </div>
  <div class="abs rider-art" role="img" aria-label="Illustration of a cowboy on a rearing horse swinging a lasso"></div>
  <div class="abs swirl-art" role="img" aria-label="Faint decorative flourish"></div>

  <div class="abs letter">
    <p class="salute">Dear [Sponsor’s Name],</p>
    <p>I hope this letter finds you well.</p>
    <p>As we reflect on the astounding success of the 2023 Cedar Ridge Rodeo, we’re filled with gratitude and excitement. Returning with a bang after a three-year hiatus, our event was hailed as “the best rodeo in the north” by contestants and attendees alike. Such accolades have fuelled our determination to raise the bar even higher.</p>
    <p>Our heartfelt thanks go out to you, our invaluable sponsors, for your unwavering support. It’s because of you that the Cedar Ridge Rodeo, a tradition cherished for over 36 years, continues to thrive and bring joy to countless cowboys, cowgirls, and rodeo enthusiasts from nearby communities and beyond. Looking ahead to 2024, we’re thrilled to introduce exciting new features, including:</p>
    <ul>
      <li>a wild pony race,</li>
      <li>mutton bustin’, <span style="font-weight:400">and</span></li>
      <li>the fantastic DJ Rowan, who will be spinning tunes alongside the much-loved Silverpine band.</li>
    </ul>
    <p>Additionally, we’re embarking on a groundbreaking project for a new Rodeo facility, set to be located just north of our community. This ambitious undertaking, slated for completion in 2025, will include state-of-the-art rodeo equipment, buildings, offices, announcer booths, and more.</p>
    <p>The Cedar Ridge Rodeo, which features two action-packed one-day events, will continue its tradition of awarding a custom buckle each day. Additionally, this year, we are excited to introduce a custom knife as a special award for the overall winner of each event. A significant part of what makes our rodeo so appealing to contestants is our substantial payout. This key aspect not only heightens the competitive spirit but also plays a crucial role in attracting a larger and more diverse group of talented participants.</p>
    <p>Your sponsorship is not just a contribution but a legacy in preserving rodeo traditions and community engagement. Funds raised will support various needs, including <b>supplies not covered by donations, ground upgrades, rodeo stock, prizes, event payouts, and more.</b></p>
    <p>Enclosed are the sponsorship levels for your consideration. This year, we’ve added the convenience of <b>Electronic Funds Transfer (EFT), E-Transfer, Credit/Debit Card or Cheque for payment options.</b> Please fill out one of the attached forms at your earliest convenience.</p>
    <p>Should you have any questions or need further information, please don’t hesitate to reach out. Together, let’s make the 2024 Cedar Ridge Rodeo a landmark event that continues to echo the rich heritage and vibrant spirit of our community.</p>
    <p>Thank you for your continued support.</p>
    <p>Warm regards,</p>
    <p class="sign">Dana Whitford<br>Cedar Ridge Rodeo Manager<br>contact@cedarridgerodeo.com</p>
  </div>
</section>

<section class="page page-levels">
  <div class="brand" style="left:22px;top:20px;width:44px;height:42px"><span class="brand-dot"></span><span class="brand-name" style="font-size:7px">Cedar Ridge<br>Rodeo</span></div>
  <div class="bronco-art" style="left:80px" role="img" aria-label="Blue illustration of a bucking bronco and rider"></div>
  <h1 class="sheet-title" style="left:122px">Base Sponsorship<br>Levels</h1>
  <div class="bronco-art" style="left:247px" role="img" aria-label="Blue illustration of a bucking bronco and rider"></div>
  <div class="brand" style="left:303px;top:20px;width:44px;height:42px"><span class="brand-dot"></span><span class="brand-name" style="font-size:7px">Cedar Ridge<br>Rodeo</span></div>

  <div class="tan-block" style="left:0;top:148px;width:137px;height:229px"></div>
  <div class="photo" style="left:22.5px;top:78px;width:157px;height:226px;background:linear-gradient(180deg,#7a5a3e,#4a3020)" role="img" aria-label="Photo of a young bull rider walking in the arena holding a helmet"></div>
  <div class="photo" style="left:189.5px;top:78px;width:156px;height:104px;background:linear-gradient(180deg,#8a8a80,#a08060)" role="img" aria-label="Photo of a barrel racer turning her horse in a cloud of dust"></div>
  <div class="photo" style="left:22.5px;top:318px;width:157px;height:104px;background:linear-gradient(135deg,#3d4c60,#6b4a30)" role="img" aria-label="Photo of a cowgirl riding a horse out of the chute"></div>

  <div class="tier-head to-dark" style="left:189.5px;top:195px;width:156px;height:16px"><svg><use href="#star"/></svg>BRONZE SUPPORTER: $1,000<svg><use href="#star"/></svg></div>
  <div class="tier-body" style="left:189.5px;top:211px;width:156px;height:37px"><ul>
    <li>Company name listed in the event program.</li>
    <li>Social media mention on all rodeo-related pages.</li>
    <li>Small logo display on the event’s main digital screen.</li>
    <li>4 Single Day Passes to the Rodeo.</li></ul></div>

  <div class="tier-head to-orange" style="left:189.5px;top:255px;width:156px;height:16px"><svg><use href="#star"/></svg>SILVER SPONSOR: $2,000<svg><use href="#star"/></svg></div>
  <div class="tier-body" style="left:189.5px;top:271px;width:156px;height:46px"><ul>
    <li>Includes all Bronze Supporter benefits.</li>
    <li>Company logo on the event website.</li>
    <li>Company banner displayed at the event (provided by the Rodeo).</li>
    <li>6 Single Day Passes to the Rodeo.</li></ul></div>

  <div class="tier-head to-dark" style="left:189.5px;top:318.5px;width:156px;height:16px"><svg><use href="#star"/></svg>GOLD PARTNER: $3,000<svg><use href="#star"/></svg></div>
  <div class="tier-body" style="left:189.5px;top:334.5px;width:156px;height:43.5px"><ul>
    <li>Includes all Silver Sponsor benefits.</li>
    <li>Medium-sized banner at the event (provided by the rodeo).</li>
    <li>6 Weekend Passes to the rodeo.</li></ul></div>

  <div class="tier-head to-orange" style="left:189.5px;top:380px;width:156px;height:16px"><svg><use href="#star"/></svg>PLATINUM CONTRIBUTOR: $6,500<svg><use href="#star"/></svg></div>
  <div class="tier-body" style="left:189.5px;top:396px;width:156px;height:32px"><ul>
    <li>Includes all Gold Partner benefits.</li>
    <li>Logo on all event materials.</li>
    <li>8 Weekend Passes with VIP seating to the Rodeo.</li></ul></div>

  <div class="tier-head to-dark" style="left:22.5px;top:432px;width:323px;height:17px;justify-content:center;gap:36px"><svg><use href="#star"/></svg>DIAMOND PATRON: $8,500<svg><use href="#star"/></svg></div>
  <div class="tier-body diamond-body" style="left:22.5px;top:449px;width:323px;height:48px">
    <ul><li>Includes all Platinum Contributor benefits.</li>
      <li>Large banner in a prime location at the event (provided by the Rodeo).</li>
      <li>Exclusive 2 VIP parking spots.</li>
      <li>12 Weekend VIP Passes to the Rodeo.</li></ul>
    <ul><li>Option to provide short Commercial for your company</li>
      <li>Option to provide short Commercial for your company</li>
      <li>A banner on one of the 6 chutes or main gates used in the arena.</li></ul>
  </div>
</section>

<section class="page page-events">
  <div class="brand" style="left:22px;top:20px;width:44px;height:42px"><span class="brand-dot"></span><span class="brand-name" style="font-size:7px">Cedar Ridge<br>Rodeo</span></div>
  <div class="bronco-art" style="left:80px" role="img" aria-label="Blue illustration of a bucking bronco and rider"></div>
  <h1 class="sheet-title" style="left:122px">Specific Event<br>Sponsorships</h1>
  <div class="bronco-art" style="left:246px" role="img" aria-label="Blue illustration of a bucking bronco and rider"></div>
  <div class="brand" style="left:302px;top:20px;width:44px;height:42px"><span class="brand-dot"></span><span class="brand-name" style="font-size:7px">Cedar Ridge<br>Rodeo</span></div>

  <div class="tan-block" style="left:232px;top:127px;width:135px;height:280px"></div>
  <div class="photo" style="left:189px;top:84.5px;width:157px;height:103px;background:linear-gradient(160deg,#7d8a94,#5a3a22)" role="img" aria-label="Photo of a saddle bronc horse bucking in the arena"></div>
  <div class="photo" style="left:189px;top:200px;width:157px;height:92px;background:linear-gradient(180deg,#6a9cb8,#6b4a30)" role="img" aria-label="Photo of a barrel racer rounding a barrel"></div>
  <div class="photo" style="left:189px;top:305px;width:157px;height:103px;background:linear-gradient(180deg,#9a9a92,#5c4632)" role="img" aria-label="Photo of a young rider from behind on horseback"></div>

  <div class="event-head to-dark" style="left:22.5px;top:84.5px;width:156px;height:31px"><svg><use href="#star"/></svg><span>Pancake Breakfast and/or<br>Burger Night Sponsor<br>(3 spots available): $2,500 each</span><svg><use href="#star"/></svg></div>
  <div class="event-body" style="left:22.5px;top:116px;width:156px"><ul>
    <li>Recognition during the sponsored event(s) and throughout the Rodeo.</li>
    <li>Banner display and promotional material distribution (provided by the Rodeo).</li>
    <li>6 Weekend Passes to the Rodeo.</li></ul></div>

  <div class="tier-body" style="left:22.5px;top:164px;width:156px;height:65px;padding:0"></div>
  <div class="event-head to-dark" style="left:22.5px;top:164px;width:156px;height:21px"><svg><use href="#star"/></svg><span>Gymkhana &amp; Kids Zone Sponsor<br>(3 spots available): $2,500 each</span><svg><use href="#star"/></svg></div>
  <div class="event-body" style="left:22.5px;top:185px;width:156px"><ul>
    <li>Recognition during the sponsored event(s) and throughout the Rodeo.</li>
    <li>Banner display and promotional material distribution (provided by the Rodeo).</li>
    <li>6 Weekend Passes to the Rodeo.</li></ul></div>

  <div class="event-head to-dark" style="left:22.5px;top:236px;width:156px;height:22px"><svg><use href="#star"/></svg><span>Prime Rib Dinner Sponsor<br>(3 spots available): $6,500 each</span><svg><use href="#star"/></svg></div>
  <div class="event-body" style="left:22.5px;top:258px;width:156px"><ul>
    <li>Recognition during the dinner and throughout the Rodeo.</li>
    <li>Banner display and promotional material distribution (provided by the Rodeo).</li>
    <li>Sponsor covers the cost of the caterer.</li>
    <li>Option to provide short Commercial for your company</li>
    <li>8 Weekend Passes with VIP seating to the Rodeo.</li></ul></div>

  <div class="tier-body" style="left:22.5px;top:329px;width:156px;height:78px;padding:0"></div>
  <div class="event-head to-dark" style="left:22.5px;top:329px;width:156px;height:22px"><svg><use href="#star"/></svg><span>Cultural Sponsor<br>(2 spots available): $6,500 each</span><svg><use href="#star"/></svg></div>
  <div class="event-body" style="left:22.5px;top:351px;width:156px"><ul>
    <li>Recognition during and throughout the Rodeo.</li>
    <li>Provide labor to help Cedar Ridge Staff with cultural events.</li>
    <li>Banner display and promotional material distribution (provided by the Rodeo).</li>
    <li>Option to provide short Commercial for your company</li>
    <li>Weekend Passes with VIP seating to the Rodeo.</li></ul></div>

  <p class="abs closing">As we enthusiastically prepare for the 2024 Cedar Ridge Rodeo at the Cedar Ridge First Nation Rodeo grounds, we are thrilled to continue the successful format from last year. This year, we’re once again expanding to a 3-day family event, maintaining our exciting Friday afternoon Gymkhana in the lineup. Join us as we continue the beloved rodeo tradition, a highlight of our community for over 35 years, bringing joy and excitement to families and rodeo enthusiasts alike.</p>

  <div class="abs quote-box">
    <div class="flourish-art" style="left:6px" role="img" aria-label="Red decorative flourish"></div>
    <div class="flourish-art" style="right:6px" role="img" aria-label="Red decorative flourish"></div>
    Different Quotes we like.
    <strong>“Cowboy is a breed tougher than nails and strong as steel.”</strong>
    <strong>“Courage is being scared to death and saddling up anyway”</strong>
    <em>Hank Morrow</em>
  </div>
</section>
</body>
</html>
```